Engineering group involved with fire safety needs a business card

We need a business card design for a company based in Greece called "Varotis Group". We are engineers and specialized technicians, operating the following : a) Fire fighting equipment trade b) Installation , Inspection & Maintenance of fire extinguishers and fire protection systems c) Occupational Health & Safety (Risk assessment & management/ Staff training). We need a clear and simple card design. I uploaded a draft I made, in order to give you an idea of the company and how I currently imagine the design of the card. I also uploaded the logo in .png file format. We are always open to different, new suggestions and ideas you may want to submit.
Target Market(s)
industries, companies, managers, retail clients
Industry/Entity Type
Fire Safety
Contact Information for Business Card
Addresses & phone numbers (headquarters + branch), logo, name (you can find all the details on the uploaded files!)
Colors
Designer to choose colors to be used in the design.
Look and feel
Each slider illustrates characteristics of the customer's brand and the style your logo design should communicate.

```html
<!DOCTYPE html>
<html lang="en">
<head>
<meta charset="utf-8">
<title>Varotis Group – Business Card</title>
<link rel="stylesheet" href="https://fonts.googleapis.com/css2?family=Montserrat:wght@600;700&family=Work+Sans:wght@400;500;600&display=swap">
<style>
  :root {
    --bg: #2a2a2a;
    --card-dark: #333334;
    --card-dark-edge: #262627;
    --card-light: #ffffff;
    --brand-red: #a8161c;
    --brand-grey: #5b5f63;
    --text-dark: #4a4a4a;
    --text-white: #ffffff;
    --text-soft: #e8e8e8;
  }
  * { margin: 0; padding: 0; box-sizing: border-box; }
  html, body { width: 1200px; height: 878px; overflow: hidden; }
  body {
    background: var(--bg);
    font-family: "Work Sans", Arial, sans-serif;
    position: relative;
  }
  .card {
    position: absolute;
    left: 250px;
    width: 700px;
    height: 400px;
    overflow: hidden;
    box-shadow: 0 10px 30px rgba(0,0,0,.45);
  }
  /* ---------- back side ---------- */
  .card--back { top: 26px; background: var(--card-dark); }
  .card__texture {
    position: absolute; inset: 0;
    background: linear-gradient(135deg, var(--card-dark-edge) 0%, #3d3d3e 50%, var(--card-dark-edge) 100%);
  }
  .back__brand {
    position: absolute; top: 92px; left: 0; right: 0;
    text-align: center; color: var(--text-white);
  }
  .brand-name {
    font-family: "Montserrat", Arial, sans-serif;
    font-weight: 700;
    font-size: 74px;
    letter-spacing: 3px;
    line-height: 1;
  }
  .brand-sub {
    display: flex; align-items: center; justify-content: center; gap: 14px;
    font-family: "Montserrat", Arial, sans-serif;
    font-weight: 600; font-size: 36px; letter-spacing: 5px;
    line-height: 1; margin-top: 4px;
  }
  .brand-sub::before, .brand-sub::after {
    content: ""; width: 120px; height: 3px; background: currentColor;
  }
  .tagline {
    font-size: 19px; letter-spacing: 1px; margin-top: 8px;
  }
  .back__services {
    position: absolute; top: 268px; left: 0; right: 0;
    text-align: center; color: var(--text-soft);
    font-size: 17px; letter-spacing: 1.2px; line-height: 1.55;
    text-transform: uppercase;
  }
  .back__services .web { text-transform: none; letter-spacing: .8px; }

  /* ---------- front side ---------- */
  .card--front { top: 452px; background: var(--card-light); }
  .front__brand {
    position: absolute; left: 40px; top: 150px; width: 300px;
    color: var(--brand-red);
  }
  .front__brand .mark-row {
    display: flex; align-items: center; gap: 12px;
  }
  .mark-square { width: 22px; height: 22px; background: var(--brand-red); flex: none; }
  .front__brand .name {
    font-family: "Montserrat", Arial, sans-serif;
    font-weight: 700; font-size: 36px; letter-spacing: 1px; line-height: 1;
    white-space: nowrap;
  }
  .front__brand .tagline {
    color: var(--brand-grey); font-size: 15px; margin-top: 14px; letter-spacing: .6px;
  }
  .front__divider {
    position: absolute; left: 362px; top: 60px; width: 2px; height: 280px;
    background: var(--brand-red);
  }
  .front__details {
    position: absolute; left: 392px; top: 58px; right: 20px;
    color: var(--text-dark); font-size: 15px; line-height: 1.3;
  }
  .person-name {
    color: var(--brand-red); font-weight: 600; font-size: 19px;
    letter-spacing: .8px; text-transform: uppercase;
  }
  .person-role { font-size: 16px; letter-spacing: .6px; }
  .contact-list { list-style: none; margin-top: 8px; }
  .contact-list li { display: flex; align-items: center; gap: 9px; letter-spacing: .5px; }
  .contact-list svg { width: 11px; height: 11px; flex: none; fill: var(--brand-red); }
  .office-label { color: var(--brand-red); font-weight: 600; margin-top: 8px; }
  .office-label + p { letter-spacing: .5px; }
</style>
</head>
<body>

<section class="card card--back" aria-label="Business card back">
  <div class="card__texture" role="img" aria-label="Dark tonal repeating brand pattern"></div>
  <div class="back__brand">
    <div class="brand-name">VAROTIS</div>
    <div class="brand-sub">GROUP</div>
    <div class="tagline">installation | inspection | maintenance</div>
  </div>
  <div class="back__services">
    <p>Fire fighting equipment | Licencing &amp; business registration</p>
    <p>Occupational health &amp; safety | Staff training</p>
    <p class="web">www.varotisgroup.gr &nbsp;info@varotisgroup.gr</p>
  </div>
</section>

<section class="card card--front" aria-label="Business card front">
  <div class="front__brand">
    <div class="mark-row">
      <span class="mark-square"></span>
      <span class="name">Varotis Group</span>
    </div>
    <div class="tagline">installation | inspection | maintenance</div>
  </div>

  <div class="front__divider"></div>

  <div class="front__details">
    <p class="person-name">Stavros Andrianos</p>
    <p class="person-role">Mechanical Engineer</p>
    <p class="person-role">OHS Consultant</p>
    <ul class="contact-list">
      <li><svg viewBox="0 0 12 12"><path d="M2.5 0.5l2 2.5-1 1.2c.8 1.6 2 2.8 3.6 3.6L8.3 6.8l2.7 2-1 2.2C5 11 1 7 1 1.5z"/></svg>+30 22920 41583</li>
      <li><svg viewBox="0 0 12 12"><path d="M3 0h6v12H3zM4 1.5v8h4v-8z"/></svg>+30 210 5527418</li>
      <li><svg viewBox="0 0 12 12"><path d="M3 1h6v3H3zM1 5h10v4H9v2H3V9H1z"/></svg>+30 694 217 35 90</li>
      <li><svg viewBox="0 0 12 12"><path d="M0 2h12v8H0zM1.2 3.2v.4L6 6.6l4.8-3V3.2L6 6z"/></svg>info@varotisgroup.gr</li>
      <li><svg viewBox="0 0 12 12"><circle cx="6" cy="6" r="5.5"/></svg>www.varotisgroup.gr</li>
    </ul>
    <p class="office-label">Headquarters:</p>
    <p>14 Kalyvion Street, 19500 Lavrio</p>
    <p class="office-label">Branch Office:</p>
    <p>22 Platanon Avenue, 15124 Marousi</p>
  </div>
</section>

</body>
</html>
```